CPA Graduation Party

I need to make simple invitation for my sister's recent success, passing the CPA (Certified Public Accountant) exam. It is a surprise party. I want very simple and professional looking invitation. My only requirements are that you don't use any graduation caps or gowns due to the fact that it's not an actual graduation. It's a series of exams that she passes. Be creative with the design but once again, keep it professional. I have attached a font called iScriptSTD. I liked the font so was thinking about using it. But it's not necessary. If you have something slimier or better, please use it.

I was planning on printing on a specific kind of paper. It's called pearlized ivory cardstock. It has a little coating and shine on it and since it's ivory, I was thinking about the main color of the invitation to be burgundy type. For example, see the following RGB: R204, G0, B102.

Party info:
Name: Ravina
Date & Time: Saturday, March 8th, 2014 at 6:00pm
Location: Seher Mahal. 418 Brambleford Lane Parsippany, NJ 07291

I know I didn't provide a lot of info for the invite but please be creative.  Use general knowledge and other formal party invites as examples. I am not looking for a name, date and location as three bullets on the card.

Also, I forgot to mention the size of the invite.  It should be 5.5x8.5.  Thank you.

• graduation caps and/or gowns

```html
<!DOCTYPE html>
<html lang="en">
<head>
<meta charset="utf-8">
<title>Surprise CPA Celebration – Ravina</title>
<link rel="stylesheet" href="https://fonts.googleapis.com/css2?family=Kalam:wght@400;700&display=swap">
<style>
  :root {
    --page: #ffffff;
    --paper-edge: #eee3e8;
    --paper-rim: #c9a9b8;
    --berry-light: #d21e6e;
    --berry: #b01058;
    --berry-deep: #6d0a3a;
    --berry-shade: #4a0628;
    --ink-title: #5c0a32;
    --ink-light: #ffffff;
    --ink-soft: #f6d3e3;
  }
  * { margin: 0; padding: 0; box-sizing: border-box; }
  html, body {
    width: 1200px; height: 847px; overflow: hidden; background: var(--page);
  }
  .invite { position: relative; width: 1200px; height: 847px; }
  .invite__paper { position: absolute; inset: 0; width: 1200px; height: 847px; }
  .invite__music-motif {
    position: absolute; left: 720px; top: 80px; width: 440px; height: 620px;
    background: radial-gradient(ellipse at 55% 45%, rgba(120, 10, 60, 0.45) 0%, rgba(120, 10, 60, 0.18) 45%, rgba(120, 10, 60, 0) 70%);
  }
  .invite__title {
    position: absolute; left: 90px; top: 106px;
    font-family: "Kalam", cursive; font-weight: 700; font-size: 78px; line-height: 1;
    text-transform: uppercase; letter-spacing: 6px;
    color: var(--ink-title);
    transform: skewX(-8deg); transform-origin: left bottom;
    text-shadow: 2px 2px 0 var(--ink-light), -1px -1px 0 rgba(255,255,255,0.6);
    border-bottom: 4px solid var(--ink-title);
    box-shadow: 0 3px 0 rgba(255,255,255,0.7);
    padding-bottom: 2px;
  }
  .invite__occasion {
    position: absolute; left: 90px; top: 228px; width: 1020px;
    font-family: "Kalam", cursive; font-weight: 400; font-size: 27px; line-height: 34px;
    color: var(--ink-soft);
  }
  .detail {
    position: absolute; left: 90px; display: flex; align-items: baseline;
    color: var(--ink-light);
    font-family: "Kalam", cursive; font-weight: 700;
  }
  .detail__label {
    font-size: 44px; line-height: 52px;
    text-decoration: underline; text-decoration-thickness: 3px; text-underline-offset: 6px;
  }
  .detail__value {
    font-size: 30px; line-height: 44px; letter-spacing: 1px; text-transform: uppercase;
  }
  .detail--name { top: 292px; }
  .detail--name .detail__value { font-size: 44px; line-height: 52px; margin-left: 14px; }
  .detail--when { top: 410px; }
  .detail--when .detail__value { margin-left: 16px; }
  .detail--where { top: 540px; align-items: flex-start; }
  .detail--where .detail__value { margin-left: 44px; margin-top: 6px; }
  .invite__note {
    position: absolute; left: 90px; top: 690px; width: 1020px;
    font-family: "Kalam", cursive; font-weight: 400; font-size: 26px; line-height: 34px;
    color: var(--ink-soft);
  }
</style>
</head>
<body>
<main class="invite">
  <svg class="invite__paper" viewBox="0 0 1200 847" aria-hidden="true">
    <defs>
      <radialGradient id="berryGlow" cx="0.3" cy="0.25" r="0.95">
        <stop offset="0" stop-color="#d21e6e"/>
        <stop offset="0.45" stop-color="#b01058"/>
        <stop offset="0.85" stop-color="#6d0a3a"/>
        <stop offset="1" stop-color="#4a0628"/>
      </radialGradient>
    </defs>
    <polygon fill="#eee3e8" stroke="#c9a9b8" stroke-width="2"
      points="16,12 120,18 260,8 400,16 560,6 720,14 880,8 1040,16 1190,10 1184,140 1192,300 1182,460 1190,620 1184,760 1188,832 1040,826 880,838 720,828 560,840 400,830 240,838 90,830 12,836 18,700 8,540 16,380 6,220 14,90"/>
    <polygon fill="url(#berryGlow)"
      points="40,36 150,42 300,32 450,40 600,30 760,40 920,32 1080,42 1164,36 1158,160 1166,320 1156,480 1164,640 1160,806 1020,800 860,812 700,802 540,812 380,804 220,812 90,804 36,810 42,660 32,500 40,340 30,190"/>
  </svg>

  <div class="invite__music-motif" role="img" aria-label="Faint music notes and treble clef decoration"></div>

  <h1 class="invite__title">Party Info:</h1>

  <p class="invite__occasion">Join us for a surprise party celebrating Ravina passing the CPA exam!</p>

  <p class="detail detail--name">
    <span class="detail__label">Name:</span>
    <span class="detail__value">Ravina</span>
  </p>

  <p class="detail detail--when">
    <span class="detail__label">Date &amp; Time:</span>
    <span class="detail__value">Saturday, March 8th, 2014 at 6:00pm</span>
  </p>

  <p class="detail detail--where">
    <span class="detail__label">Location:</span>
    <span class="detail__value">Seher Mahal. 418 Brambleford Lane<br>Parsippany, NJ 07291</span>
  </p>

  <p class="invite__note">Shh… it's a surprise! Please arrive early and keep it a secret.</p>
</main>
</body>
</html>
```